Defense Attorney Business Card Design Project/ Stationary

I am looking for a distinctive business card design for my solo law practice.
I practice criminal defense, both juvenile and adult, including DUI. I am a very experienced attorney with prior military experience. The design should convey a traditional, old school flair, but not be too stodgy or uptight. Some color. My logo should appear.

Project Deadline Extended Reason: I misunderstood how this project works and I was not prepared with my logo when this project ran the first time. Added Thursday, November 13, 2014

Reason: I was sent overseas on military duty last year, which interrupted this project. Thank you for your participation... I hope we can get this done this week! Thank you, Des

Target Market(s)

Regular everyday people looking for strong, knowledgeable, authoritative representation while they are faced with criminal charges. Many have never been charged with a crime before. A reassuring air is therefore desired.

Industry/Entity Type

Business

Contact Information for Business Card

My information is:
Desmond R. Whitcombe, Attorney at Law
735 Linden Avenue Suite 300
Oakland, California 94618
Tel: (510) 555-0183
Fax: (510) 555-0162
email: deswhitcombelaw@mailbrook.net
web: www.deswhitcombelaw.net

Font styles to use
Serif
Sans Serif
Decorative

Colors
0255a3
ffffff

Requirements
Must have
• Sharp lines, bold elements. Conservative use of colors, such as deep blues, burgundy, grays for example.
• While my logo says "Des Whitcombe", it should be modified to show "Desmond R. Whitcombe".
Should not have
• Cliche imagery such as scales of justice, gavels, Tower of Varenholt, etc.

```html
<!DOCTYPE html>
<html lang="en">
<head>
<meta charset="utf-8">
<title>Desmond R. Whitcombe, Attorney at Law — Business Card</title>
<link rel="stylesheet" href="https://fonts.googleapis.com/css2?family=Michroma&display=swap">
<style>
  :root {
    --canvas: #e9eaec;
    --card: #ffffff;
    --card-edge: #d7d9dc;
    --navy: #1d4a6a;
    --swoosh: #6c6f73;
    --text: #5d6166;
    --text-strong: #2f3438;
    --divider: #b9bcc0;
  }
  * { box-sizing: border-box; margin: 0; padding: 0; }
  html, body { width: 1200px; height: 900px; overflow: hidden; }
  body {
    background: var(--canvas);
    font-family: "Michroma", sans-serif;
    color: var(--text);
    position: relative;
  }
  .card {
    position: absolute;
    top: 280px;
    width: 520px;
    height: 340px;
    background: var(--card);
    border-radius: 40px;
    overflow: hidden;
    box-shadow: 0 0 0 1px var(--card-edge), 0 10px 24px rgba(0,0,0,0.12);
  }
  .card--front { left: 50px; }
  .card--back { left: 630px; }

  .front-shapes { position: absolute; inset: 0; }

  .identity {
    position: absolute;
    right: 258px;
    top: 118px;
    text-align: right;
    white-space: nowrap;
  }
  .identity__name {
    font-size: 10px;
    letter-spacing: 1px;
    color: var(--text-strong);
    text-transform: uppercase;
  }
  .identity__title {
    font-size: 8px;
    letter-spacing: 1px;
    margin-top: 6px;
  }
  .address {
    position: absolute;
    right: 258px;
    top: 170px;
    text-align: right;
    white-space: nowrap;
    font-size: 8px;
    letter-spacing: 1px;
    line-height: 16px;
    text-transform: uppercase;
  }
  .divider {
    position: absolute;
    left: 272px;
    top: 112px;
    width: 1px;
    height: 118px;
    background: var(--divider);
  }
  .contacts {
    position: absolute;
    left: 286px;
    top: 116px;
    list-style: none;
    font-size: 7.5px;
    letter-spacing: 0.3px;
    white-space: nowrap;
  }
  .contacts li {
    display: flex;
    align-items: center;
    height: 24px;
  }
  .contacts .icon {
    width: 11px;
    height: 11px;
    margin-right: 8px;
    flex: none;
  }
  .contacts .web { padding-left: 19px; }

  .brand {
    position: absolute;
    inset: 0;
    display: flex;
    flex-direction: column;
    align-items: center;
    justify-content: center;
    color: var(--navy);
    font-size: 18px;
    letter-spacing: 2px;
    line-height: 34px;
    text-align: center;
    white-space: nowrap;
  }
  .brand__dot {
    width: 58px;
    height: 58px;
    border-radius: 50%;
    background: var(--navy);
    margin-bottom: 18px;
  }
</style>
</head>
<body>

<section class="card card--front" aria-label="Business card front">
  <svg class="front-shapes" width="520" height="340" viewBox="0 0 520 340">
    <path d="M0 0 H210 C100 30 25 110 0 240 Z" fill="var(--navy)"/>
    <path d="M228 0 C112 36 36 118 16 250" fill="none" stroke="var(--swoosh)" stroke-width="5"/>
    <path d="M300 340 C395 322 470 292 520 230 V340 Z" fill="var(--navy)"/>
  </svg>

  <div class="identity">
    <p class="identity__name">Desmond R. Whitcombe</p>
    <p class="identity__title">Attorney at Law</p>
  </div>

  <p class="address">735 Linden Avenue<br>Suite 300<br>Oakland, CA 94618</p>

  <div class="divider"></div>

  <ul class="contacts">
    <li><svg class="icon" viewBox="0 0 12 12"><circle cx="6" cy="6" r="6" fill="var(--navy)"/><path d="M4 3.2 L5.2 4.6 L4.6 5.4 Q5.6 7 6.8 7.6 L7.6 7 L9 8.2 L8.2 9.2 Q5 8.6 3 4.2 Z" fill="#fff"/></svg>Tel (510) 555-0183</li>
    <li><svg class="icon" viewBox="0 0 12 12"><circle cx="6" cy="6" r="6" fill="var(--navy)"/><rect x="3" y="3.5" width="6" height="5" rx="0.6" fill="#fff"/><rect x="4" y="2.5" width="4" height="1.5" fill="#fff"/></svg>Fax (510) 555-0162</li>
    <li><svg class="icon" viewBox="0 0 12 12"><circle cx="6" cy="6" r="6" fill="var(--navy)"/><rect x="3" y="4" width="6" height="4.2" fill="#fff"/><path d="M3 4 L6 6.4 L9 4" fill="none" stroke="var(--navy)" stroke-width="0.7"/></svg>deswhitcombelaw@mailbrook.net</li>
    <li class="web">www.deswhitcombelaw.net</li>
  </ul>
</section>

<section class="card card--back" aria-label="Business card back">
  <div class="brand">
    <span class="brand__dot"></span>
    <span>DESMOND R. WHITCOMBE</span>
    <span>LAW</span>
  </div>
</section>

</body>
</html>
```